Website Design for R M Builders: Showcasing Excellence in General Contracting

R M Builders, a leading general contractor based in California, is seeking a professional and engaging website design to effectively showcase our expertise, services, and commitment to excellence. The website will serve as a digital platform to represent our brand identity, highlight our portfolio, and attract potential clients in various sectors.

Key Objectives:

Reflect Company Identity: The website should accurately reflect the identity and values of R M Builders, including our dedication to quality, professionalism, and client satisfaction.
Showcase Services: Highlight our wide range of general contracting services, including but not limited to construction management, design-build, renovation, and commercial construction.
Portfolio Display: Display an extensive portfolio of past projects completed by R M Builders, showcasing our capabilities, craftsmanship, and successful outcomes.
Client Testimonials: Incorporate client testimonials and case studies to demonstrate our track record of delivering projects on time, within budget, and to the highest standards.
Contact Information: Ensure easy access to contact information, including phone number, email, and physical address, to facilitate communication with potential clients.
Responsive Design: Develop a responsive website design optimized for various devices and screen sizes, ensuring a seamless user experience across desktops, laptops, tablets, and smartphones.
Search Engine Optimization (SEO): Implement SEO best practices to enhance the visibility of the website on search engines, increasing organic traffic and generating leads.
User-Friendly Navigation: Create an intuitive and user-friendly navigation structure that enables visitors to easily find the information they need, such as services, portfolio, testimonials, and contact details.
Visual Appeal: Utilize visually appealing graphics, images, and layout designs to capture the attention of visitors and leave a lasting impression of professionalism and quality.
Compliance and Security: Ensure compliance with industry standards and regulations, as well as implementing necessary security measures to protect user data and privacy.

```html
<!DOCTYPE html>
<html lang="en">
<head>
<meta charset="utf-8">
<title>R M Builders — General Contracting</title>
<link href="https://fonts.googleapis.com/css2?family=Archivo:wght@700;800;900&family=Poppins:wght@400;500;600;700&display=swap" rel="stylesheet">
<style>
:root{
  --navy:#223369;
  --navy-deep:#1b2a5c;
  --band:#2a3f7a;
  --sky:#08a3e6;
  --sky-soft:#d8f0fb;
  --orange:#e8a23a;
  --ink:#1e1e1e;
  --muted:#555;
  --white:#fff;
  --black:#0b0b0b;
  --head:"Archivo",sans-serif;
  --body:"Poppins",sans-serif;
}
*{box-sizing:border-box;margin:0;padding:0}
html,body{width:1200px;height:4648px;overflow:hidden}
body{font-family:var(--body);color:var(--ink);background:var(--white);position:relative}
.abs{position:absolute}
.btn{position:absolute;display:flex;align-items:center;justify-content:center;font-family:var(--body);font-weight:700;font-size:14px;letter-spacing:.5px;border-radius:3px}
.btn-light{background:var(--white);color:var(--navy)}
.btn-dark{background:var(--navy);color:var(--white)}
.dots{display:flex;gap:6px}
.dots span{width:20px;height:20px;border-radius:50%;background:var(--white);display:block}

/* header */
.topbar{position:absolute;left:0;top:0;width:1200px;height:82px;background:var(--navy)}
.topbar .mail{left:140px;top:16px;color:var(--white);font-size:14px;line-height:24px}
.topbar .dots{position:absolute;left:770px;top:30px}
.contacts-btn{left:970px;top:24px;width:118px;height:34px;background:var(--white);color:var(--ink);font-size:12px}
.navbar{position:absolute;left:0;top:82px;width:1200px;height:63px;background:var(--white)}
.navbar a{position:absolute;top:18px;font-size:15px;color:var(--ink);text-decoration:none}
.brand-tab{position:absolute;left:523px;top:0;width:154px;height:182px;background:var(--white);border-radius:0 0 77px 77px;display:flex;flex-direction:column;align-items:center;justify-content:center;gap:8px;z-index:3}
.brand-tab .sq{width:46px;height:46px;background:var(--navy)}
.brand-tab .name{font-family:var(--body);font-weight:700;font-size:16px;color:var(--ink)}
.brand-tab .loc{font-family:var(--body);font-weight:700;font-size:11px;color:var(--ink)}

/* hero */
.hero{position:absolute;left:0;top:145px;width:1200px;height:644px;background:linear-gradient(180deg,#3a4150 0%,#6b4a3a 40%,#c56a2a 58%,#4a3b33 80%,#2b2a2a 100%)}
.hero h1{left:110px;top:190px;font-family:var(--head);font-weight:900;font-size:42px;line-height:43px;color:var(--white);text-transform:uppercase}
.hero p{left:110px;top:335px;width:480px;font-size:15px;line-height:26px;color:var(--white)}
.hero .btn{left:110px;top:415px;width:146px;height:38px;color:var(--ink)}

/* about */
.about-photo{left:112px;top:872px;width:419px;height:323px;border-radius:14px;background:linear-gradient(135deg,#6f7a6a,#b28a5a 55%,#4b4a48)}
.about-wave{left:112px;top:1160px;width:419px;height:96px}
.about h2{left:601px;top:858px;font-family:var(--head);font-weight:800;font-size:33px;color:var(--navy)}
.about h3{left:601px;top:908px;font-size:19px;font-weight:600;color:var(--black)}
.about p{left:601px;top:958px;width:495px;font-size:14px;line-height:31px;color:var(--ink)}
.about .btn{left:601px;top:1157px;width:146px;height:38px}

/* services */
.services{position:absolute;left:0;top:1282px;width:1200px;height:725px;background:linear-gradient(180deg,#2c4180,#233770)}
.sec-title{position:absolute;left:0;width:1200px;text-align:center;font-family:var(--head);font-weight:800;font-size:33px}
.sec-sub{position:absolute;left:0;width:1200px;text-align:center;font-weight:600;font-size:19px}
.rule{position:absolute;left:547px;width:106px;height:3px;background:var(--orange)}
.svc-card{position:absolute;top:212px;width:222px;height:343px;background:var(--white);border-radius:8px;text-align:center}
.svc-card .icon{position:absolute;left:55px;top:-54px;width:112px;height:112px;border-radius:50%;background:var(--white);display:flex;align-items:center;justify-content:center}
.svc-card .icon span{width:64px;height:64px;border-radius:50%;border:3px solid var(--sky);display:flex;align-items:center;justify-content:center}
.svc-card h4{margin-top:68px;font-size:17px;font-weight:600;color:var(--black)}
.svc-card p{margin:10px auto 0;width:182px;font-size:14px;line-height:24px;color:var(--muted)}
.svc-card .more{margin-top:18px;font-size:11px;color:var(--sky);letter-spacing:.4px}
.arrow-ring{position:absolute;top:394px;width:36px;height:36px;border:2px solid var(--white);border-radius:50%}

/* general */
.general h2{left:110px;top:2088px;font-family:var(--head);font-weight:800;font-size:33px;color:var(--navy)}
.general h3{left:110px;top:2137px;font-size:19px;font-weight:600;color:var(--navy)}
.general .rule{left:110px;top:2175px;width:106px}
.general .lead{left:110px;top:2204px;width:500px;font-size:15px;line-height:29px}
.general .small{left:110px;top:2274px;width:500px;font-size:12px;line-height:28px}
.feat{position:absolute;display:flex;gap:18px}
.feat .ic{width:50px;height:50px;border-radius:6px;background:#ececec}
.feat b{display:block;font-size:16px;font-weight:600;color:var(--black);margin-top:4px}
.feat span{font-size:14px;color:var(--muted)}
.general .btn{left:112px;top:2532px;width:146px;height:40px}
.general-photo{left:657px;top:2090px;width:431px;height:414px;background:linear-gradient(135deg,#c9d6e2,#7e97b5 55%,#3d4f6e)}
.general-wave{left:657px;top:2480px;width:431px;height:96px}

/* portfolio */
.portfolio{position:absolute;left:0;top:2659px;width:1200px;height:919px;background:linear-gradient(180deg,#2c4180,#223669)}
.tile{position:absolute;width:233px;height:256px;border-radius:3px}
.tile.feature{background:linear-gradient(180deg,#20a9df,#1a8ac6);display:flex;align-items:center;justify-content:center;text-align:center;color:var(--white);font-family:var(--head);font-weight:700;font-size:21px;line-height:26px;padding:0 24px}

/* testimonials */
.tcard{position:absolute;top:3785px;width:314px;height:372px;background:var(--white);box-shadow:0 6px 22px rgba(0,0,0,.12);text-align:center}
.tcard .q{position:absolute;left:10px;top:8px;font-family:var(--head);font-size:54px;line-height:54px;color:var(--navy)}
.tcard p{position:absolute;left:22px;top:62px;width:270px;font-size:14px;line-height:20px;color:var(--ink)}
.tcard .foot{position:absolute;left:0;bottom:0;width:314px;height:128px}
.tcard .avatar{position:absolute;left:113px;top:196px;width:88px;height:88px;border-radius:50%;border:4px solid var(--white);z-index:2}
.tcard .who{position:absolute;left:0;top:74px;width:314px;font-weight:600;font-size:14px;color:var(--white)}
.tcard .dots{position:absolute;left:107px;top:100px}
.tcard .dots span{width:18px;height:18px}

/* footer */
.footer{position:absolute;left:0;top:4325px;width:1200px;height:323px;background:var(--black);color:var(--white)}
.footer .brand{position:absolute;left:180px;top:56px;width:120px;display:flex;flex-direction:column;align-items:center;gap:8px}
.footer .brand .sq{width:44px;height:44px;background:var(--white)}
.footer .brand .name{font-weight:700;font-size:16px}
.footer .brand .loc{font-weight:700;font-size:11px}
.footer .dots{position:absolute;left:146px;top:212px;gap:20px}
.footer h5{position:absolute;top:66px;font-family:var(--body);font-weight:600;font-size:21px;letter-spacing:.5px}
.footer ul{position:absolute;top:110px;list-style:none;font-size:15px;line-height:26px}
.footer .contact{position:absolute;left:872px;display:flex;align-items:center;gap:14px;font-size:15px}
.footer .line{position:absolute;left:112px;top:260px;width:988px;height:1px;background:#555}
.footer .copy{position:absolute;left:0;top:278px;width:1200px;text-align:center;font-size:15px}
</style>
</head>
<body>

<header>
  <div class="topbar">
    <div class="abs mail">E-mail<br>office@rmbuilders.example</div>
    <div class="dots"><span></span><span></span><span></span><span></span></div>
    <div class="btn contacts-btn">CONTACTS</div>
  </div>
  <nav class="navbar">
    <a style="left:110px">Home</a>
    <a style="left:209px">About</a>
    <a style="left:315px">Experience</a>
    <a style="left:737px;top:22px">Services</a>
    <a style="left:861px;top:22px">Our Clients</a>
    <a style="left:1004px;top:22px">Projects</a>
  </nav>
  <div class="brand-tab">
    <div class="sq"></div>
    <div class="name">R M Builders</div>
    <div class="loc">RIDGEVIEW, CA</div>
  </div>
</header>

<section class="hero" role="img" aria-label="Excavator on a construction site at sunset">
  <h1 class="abs">Welcome to<br>since 2013<br>R M Builders</h1>
  <p class="abs">If you use this site regularly and would like to help keep the site on the Internet</p>
  <div class="btn btn-light">BOOK NOW</div>
</section>

<section class="about">
  <svg class="abs about-wave" viewBox="0 0 419 96" preserveAspectRatio="none"><path d="M10 96 C0 60 20 40 60 40 L419 30 L419 96 Z" fill="#d8f0fb"/></svg>
  <div class="abs about-photo" role="img" aria-label="Smiling construction workers in hard hats on site"></div>
  <h2 class="abs">ABOUT US</h2>
  <h3 class="abs">Welcome To Construction Company</h3>
  <p class="abs">With vast experience in the trades, site superintendence, safety, quality control, and all aspects of general contracting, R M Builders can plan, manage and execute building construction projects in all sizes under any delivery method: design-build, CM at Risk, or design-bid-build.</p>
  <div class="btn btn-dark">READ MORE</div>
</section>

<section class="services" role="region" aria-label="Our services">
  <h2 class="sec-title" style="top:78px;color:var(--white)">OUR SERVICES</h2>
  <p class="sec-sub" style="top:126px;color:var(--white)">Lorem ipsum dolor sit amet consectetur</p>
  <div class="arrow-ring" style="left:38px"></div>
  <div class="arrow-ring" style="left:1126px"></div>
  <div class="svc-card" style="left:112px"><div class="icon"><span></span></div><h4>Concrete</h4><p>Lorem Ipsum is simply dummy text of the printing and typesetting industry. Lorem Ipsum has been the industry's standard dummy text</p><div class="more">READ MORE &rarr;</div></div>
  <div class="svc-card" style="left:363px"><div class="icon"><span></span></div><h4>Remodels</h4><p>Lorem Ipsum is simply dummy text of the printing and typesetting industry. Lorem Ipsum has been the industry's standard dummy text</p><div class="more">READ MORE &rarr;</div></div>
  <div class="svc-card" style="left:615px"><div class="icon"><span></span></div><h4>Site work</h4><p>Lorem Ipsum is simply dummy text of the printing and typesetting industry. Lorem Ipsum has been the industry's standard dummy text</p><div class="more">READ MORE &rarr;</div></div>
  <div class="svc-card" style="left:866px"><div class="icon"><span></span></div><h4>SCIF</h4><p>Lorem Ipsum is simply dummy text of the printing and typesetting industry. Lorem Ipsum has been the industry's standard dummy text</p><div class="more">READ MORE &rarr;</div></div>
  <div class="btn btn-light" style="left:527px;top:599px;width:146px;height:40px">VIEW ALL</div>
</section>

<section class="general">
  <h2 class="abs">GENERAL CONTRACTING</h2>
  <h3 class="abs">Lorem ipsum dolor sit amet consectetur</h3>
  <div class="rule"></div>
  <p class="abs lead">I must explain to you how all this mistaken idea of denouncing pleasure and praising pain was born and I will give.</p>
  <p class="abs small">I must explain to you how all this mistaken idea of denouncing pleasure and praising pain was born and I will give you a complete account of the system, and expound the actual teachings.</p>
  <div class="feat" style="left:112px;top:2375px"><div class="ic"></div><div><b>design-build</b><span>Lorem ipsum dolor</span></div></div>
  <div class="feat" style="left:394px;top:2375px"><div class="ic"></div><div><b>Project Management</b><span>Lorem ipsum dolor</span></div></div>
  <div class="feat" style="left:112px;top:2452px"><div class="ic"></div><div><b>Safety Management</b><span>Lorem ipsum dolor</span></div></div>
  <div class="feat" style="left:394px;top:2452px"><div class="ic"></div><div><b>Estimating</b><span>Lorem ipsum dolor</span></div></div>
  <div class="btn btn-dark">VIEW ALL</div>
  <svg class="abs general-wave" viewBox="0 0 431 96" preserveAspectRatio="none"><path d="M0 96 L0 40 C80 0 200 10 431 40 L431 96 Z" fill="#d8f0fb"/></svg>
  <div class="abs general-photo" role="img" aria-label="Team reviewing blueprints in an office"></div>
</section>

<section class="portfolio" role="region" aria-label="Our portfolio">
  <h2 class="sec-title" style="top:80px;color:var(--white)">OUR PORTFOLIO</h2>
  <p class="sec-sub" style="top:128px;color:var(--white)">Lorem ipsum dolor sit amet consectetur</p>
  <div class="rule" style="top:165px"></div>
  <div class="tile" style="left:112px;top:211px;background:linear-gradient(135deg,#d8d8d2,#8d8c86)" role="img" aria-label="Hands reviewing architectural plans"></div>
  <div class="tile" style="left:359px;top:211px;background:linear-gradient(180deg,#d9b98a,#7c8c4a)" role="img" aria-label="Workers in safety vests at a steel structure"></div>
  <div class="tile" style="left:614px;top:211px;background:linear-gradient(135deg,#e6e4e0,#a9a6a0)" role="img" aria-label="Engineers working at a desk from above"></div>
  <div class="tile" style="left:856px;top:211px;background:linear-gradient(135deg,#c8c6c0,#c36a3a)" role="img" aria-label="Crew in hard hats around a plan table"></div>
  <div class="tile" style="left:112px;top:492px;background:linear-gradient(180deg,#5a6f9a,#c89050)" role="img" aria-label="Worker in hard hat against the sky"></div>
  <div class="tile" style="left:359px;top:492px;background:linear-gradient(135deg,#8a7864,#3a3532)" role="img" aria-label="Two professionals with a tablet on site"></div>
  <div class="tile feature" style="left:608px;top:492px;width:233px">Desert Air Base Task Orders Awarded: 5 Total Awarded Value: $3,124,332</div>
  <div class="tile" style="left:856px;top:492px;background:linear-gradient(135deg,#dfe3e6,#8b96a0)" role="img" aria-label="Architects examining a building model"></div>
  <div class="btn btn-light" style="left:527px;top:792px;width:146px;height:40px">VIEW ALL</div>
</section>

<section class="testimonials">
  <h2 class="sec-title" style="top:3650px;color:var(--navy)">OUR TESTIMONIALS</h2>
  <p class="sec-sub" style="top:3698px;color:var(--navy)">Lorem ipsum dolor sit amet consectetur</p>
  <div class="rule" style="top:3736px"></div>

  <div class="tcard" style="left:110px">
    <div class="q">&ldquo;</div>
    <p>"Lorem ipsum dolor sit amet, consectetur adipiscing elit, sed do eiusmod tempor incididunt ut labore et dolore magna aliqua. Ut enim ad minim veniam, quis nostrud exercitation ullamco laboris</p>
    <div class="avatar" style="background:#b08a6a" role="img" aria-label="Portrait of client"></div>
    <div class="foot" style="background:var(--sky)"><div class="who">DANA WHITFIELD</div><div class="dots"><span></span><span></span><span></span><span></span></div></div>
  </div>
  <div class="tcard" style="left:442px">
    <div class="q">&ldquo;</div>
    <p>"Lorem ipsum dolor sit amet, consectetur adipiscing elit, sed do eiusmod tempor incididunt ut labore et dolore magna aliqua. Ut enim ad minim veniam, quis nostrud exercitation ullamco laboris</p>
    <div class="avatar" style="background:#c9a27a" role="img" aria-label="Portrait of client"></div>
    <div class="foot" style="background:var(--navy)"><div class="who">MARIA LOPEZ</div><div class="dots"><span></span><span></span><span></span><span></span></div></div>
  </div>
  <div class="tcard" style="left:776px">
    <div class="q">&ldquo;</div>
    <p>"Lorem ipsum dolor sit amet, consectetur adipiscing elit, sed do eiusmod tempor incididunt ut labore et dolore magna aliqua. Ut enim ad minim veniam, quis nostrud exercitation ullamco laboris</p>
    <div class="avatar" style="background:#8a5a44" role="img" aria-label="Portrait of client"></div>
    <div class="foot" style="background:var(--sky)"><div class="who">OMAR BENNETT</div><div class="dots"><span></span><span></span><span></span><span></span></div></div>
  </div>
  <div class="btn btn-dark" style="left:527px;top:4200px;width:146px;height:40px">VIEW ALL</div>
</section>

<footer class="footer">
  <div class="brand"><div class="sq"></div><div class="name">R M Builders</div><div class="loc">RIDGEVIEW, CA</div></div>
  <div class="dots"><span></span><span></span><span></span><span></span><span></span></div>
  <h5 style="left:438px">COMPANY</h5>
  <ul style="left:438px"><li>Home</li><li>About us</li><li>Services</li><li>Our Portfolio</li><li>Contact Us</li></ul>
  <h5 style="left:607px">OUR SERVICES</h5>
  <ul style="left:607px;line-height:27px"><li>Air conditioning</li><li>Hearing</li><li>Heat Pumps</li><li>Ductless mini Splits</li><li>Controls</li></ul>
  <h5 style="left:870px">CONTACTS</h5>
  <div class="contact" style="top:112px">
    <svg width="22" height="24" viewBox="0 0 22 24"><path d="M11 1a8 8 0 0 0-8 8c0 6 8 14 8 14s8-8 8-14a8 8 0 0 0-8-8z" fill="#fff"/><circle cx="11" cy="9" r="3" fill="#0b0b0b"/></svg>Lakeside</div>
  <div class="contact" style="top:154px">
    <svg width="22" height="18" viewBox="0 0 22 18"><rect x="1" y="1" width="20" height="16" rx="2" fill="none" stroke="#fff" stroke-width="2"/><path d="M2 3l9 7 9-7" fill="none" stroke="#fff" stroke-width="2"/></svg>office@rmbuilders.example</div>
  <div class="contact" style="top:196px">
    <svg width="22" height="22" viewBox="0 0 22 22"><path d="M5 2l4 4-2 3c1 3 3 5 6 6l3-2 4 4-3 3C9 20 2 13 2 5z" fill="none" stroke="#fff" stroke-width="1.8"/></svg>+1(555) 240 1180</div>
  <div class="line"></div>
  <div class="copy">Copyright &copy; 2024 R M Builders. All Rights Reserved</div>
</footer>

</body>
</html>
```